Zielgruppe
TECHNIKVERLEIH
EVENTMANAGEMENT
BETRIEBSSICHERHEIT
VERANSTALTUNGSSERVICE
SOLAR
Aufgabenstellung
Texte anhand der 'auftrag_o42unpfuask7_lunoquart.pdf', Teaser Text für die Startseite selbst bestimmen, Farben anhand der Logos im Anhand und Ausgabe für Photoshop, XD oder PDF
Designt werden sollen die Startseite sowie eine Unterseite.

```html
<!DOCTYPE html>
<html lang="de">
<head>
<meta charset="utf-8">
<title>Lunoquart GmbH</title>
<link href="https://fonts.googleapis.com/css2?family=Montserrat:wght@400;500;600;700&display=swap" rel="stylesheet">
<style>
:root{
  --ink:#111;
  --text:#2b2b2b;
  --accent:#b3c620;
  --dot-red:#e3161b;
  --panel:#f4f4f4;
  --band:#9b9b9b;
  --icon-bg:#ece9f3;
}
*{margin:0;padding:0;box-sizing:border-box}
html,body{width:1200px;height:2301px;overflow:hidden;background:#fff}
body{position:relative;font-family:"Montserrat",sans-serif;color:var(--text)}
.abs{position:absolute}

.hero-panel{left:0;top:0;width:600px;height:530px;background:var(--panel)}
.hero-photo{left:600px;top:0;width:600px;height:600px;background:linear-gradient(180deg,#cfcac2 0%,#e8e1d6 40%,#d9cdb8 60%,#f3f1ee 100%)}
.brand{display:flex;align-items:center;gap:8px;font-weight:700;color:var(--ink);letter-spacing:1px;white-space:nowrap}
.brand .mark{width:13px;height:13px;background:var(--accent)}
.brand-top{left:105px;top:56px;font-size:19px}
.nav-bg{left:600px;top:45px;width:499px;height:49px;background:#fff}
.nav{left:274px;top:45px;height:49px;width:818px;display:flex;align-items:center;justify-content:space-between;font-size:11.5px;color:#333;white-space:nowrap}
.nav .active{font-weight:600;color:var(--ink);position:relative}
.nav .active::before{content:"";position:absolute;left:0;top:-8px;width:7px;height:7px;border-radius:50%;background:var(--dot-red)}
.hero-title{left:104px;top:208px;font-size:35px;line-height:40px;font-weight:700;color:var(--ink)}
.hero-title span{color:var(--accent)}
.more{left:527px;top:560px;font-size:14px;color:var(--ink);border-bottom:1px solid var(--ink);padding-bottom:1px}

.dots{background:#f6f6f6}
.photo-a{left:152px;top:703px;width:409px;height:264px;background:linear-gradient(160deg,#b6892f,#d9a13a 55%,#8a5a1e)}
.photo-b{left:586px;top:703px;width:408px;height:264px;background:linear-gradient(180deg,#b8d3e6,#9bb8c9 45%,#e3e6ea)}
.intro-card{left:105px;top:970px;width:773px;height:251px;background:#fff;box-shadow:0 40px 60px rgba(0,0,0,.08);padding:30px 36px 0 45px;font-size:13.6px;line-height:26.7px}
.intro-card b,.story b{font-weight:600;color:var(--ink)}

.story-panel{left:276px;top:1340px;width:924px;height:651px;background:var(--panel)}
.photo-c{left:152px;top:1431px;width:372px;height:454px;background:linear-gradient(170deg,#8a3a18,#c26a2f 45%,#9fb8b2 80%,#e9e4de);box-shadow:0 25px 40px rgba(0,0,0,.2)}
.story{left:607px;top:1508px;width:330px;font-size:14px;line-height:31.7px}

.footer-brand{left:214px;top:2110px;font-size:22px}
.f-head{font-size:12px;font-weight:700;color:var(--ink);letter-spacing:.3px}
.f-head::after{content:"";display:block;width:66px;height:1px;background:var(--accent);margin-top:7px}
.f-links{font-size:12.5px;color:#333;list-style:none}
.f-links li{position:absolute;white-space:nowrap}
.social li{display:flex;align-items:center;gap:14px}
.social .ico{width:26px;height:26px;border-radius:50%;background:var(--icon-bg)}
.copy{left:0;top:2249px;width:1200px;height:52px;background:var(--band);color:#eee;font-size:12.5px;display:flex;align-items:center;justify-content:center}
</style>
</head>
<body>
<div class="abs hero-panel"></div>
<div class="abs hero-photo" role="img" aria-label="Festlich eingedeckter Saal mit weißen Stühlen, Blumen und Glasdach"></div>
<div class="abs nav-bg"></div>
<div class="abs brand brand-top"><span class="mark"></span>LUNOQUART</div>
<nav class="abs nav">
  <span class="active">Lunoquart GmbH</span>
  <span>Firmenbeschreibung</span>
  <span>Veranstaltungsservice</span>
  <span>Technikverleih</span>
  <span>Eventmanagement</span>
  <span>Betriebssicherheit</span>
  <span>Solar</span>
</nav>
<h1 class="abs hero-title">Lunoquart GmbH -<br><span>Veranstaltungstechnik,<br>Eventmanagement<br>und Betriebssicherheit<br>aus einer Hand</span></h1>
<a class="abs more">Mehr</a>

<div class="abs dots" style="left:128px;top:678px;width:124px;height:228px"></div>
<div class="abs dots" style="left:894px;top:710px;width:122px;height:282px"></div>
<div class="abs photo-a" role="img" aria-label="Innenraum einer Kirche mit Stuhlreihen"></div>
<div class="abs photo-b" role="img" aria-label="Hochzeitsbogen mit Blumen und Stühlen am Meer"></div>
<div class="abs intro-card">
  <p><b>Als etabliertes</b> Unternehmen in der Eventbranche bieten wir flexible Komplettlösungen für Veranstaltungen, Events und die Durchführung größerer TV-Ereignisse. Unsere Kunden profitieren dabei von unserem Rundumservice, der sich gleichzeitig auf multiple Bereiche des Eventmanagements konzentriert. Neben der Planung und Durchführung von Veranstaltungen bieten wir einen umfangreichen Technikverleih, Lösungen für die Sicherheit in Ihrem Betrieb und auf Ihren Veranstaltungen sowie umfassende Beratung inklusive anschließender Konzeptionierung durch unser engagiertes Team aus Ingenieuren, Veranstaltungstechnikern, Bühnenhandwerkern und Designern.</p>
</div>

<div class="abs story-panel"></div>
<div class="abs dots" style="left:492px;top:1406px;width:60px;height:352px;background:#ececec"></div>
<div class="abs photo-c" role="img" aria-label="Festsaal mit Lichterketten, Blumen und gedeckten Tischen"></div>
<p class="abs story"><b>Ebenso stolz wie</b> auf unsere Reputation bei kleineren Unternehmen sowie großen Medienhäusern wie RVK, ZTN, WBL und RSX sind wir auf die jüngste Sparte der Lunoquart GmbH. Mit unseren innovativen Lösungen für Solarkraftwerke und Photovoltaik-Anlagen erfüllen wir unsere Pflicht als verantwortungsbewusstes Unternehmen, den Ausbau alternativer Energien zu unterstützen</p>

<div class="abs brand footer-brand"><span class="mark"></span>LUNOQUART</div>
<div class="abs f-head" style="left:425px;top:2056px">SCHNELLLINK</div>
<ul class="abs f-links" style="left:425px;top:2100px">
  <li style="left:0;top:0">Lunoquart GmbH</li>
  <li style="left:0;top:27px">Firmenbeschreibung</li>
  <li style="left:0;top:57px">Veranstaltungsservice</li>
  <li style="left:0;top:86px">Technikverleih</li>
  <li style="left:216px;top:0">Eventmanagement</li>
  <li style="left:216px;top:28px">Betriebssicherheit</li>
  <li style="left:217px;top:57px">Solar</li>
</ul>
<div class="abs f-head" style="left:822px;top:2056px">SOZIALEN MEDIEN</div>
<ul class="abs f-links social" style="left:827px;top:2098px">
  <li style="left:0;top:0"><span class="ico"></span>Plaudernetz</li>
  <li style="left:0;top:32px"><span class="ico"></span>Kontaktring</li>
  <li style="left:0;top:65px"><span class="ico"></span>Zwitscherpost</li>
</ul>
<div class="abs copy">© Copyright 2022 Lunoquart GmbH. Alle Rechte vorbehalten</div>
</body>
</html>
```